Change the world and help build JumpKOV.tv!

We need a mobile website design for our Beta release - see wireframes attached.
See our Logo design files attached along with fonts, etc.
Please see enclosed .PDF that provides a great overview of our company, KOV.
Any questions, feel free to ask - we're very engaged here on Pixel Harbor and will make ourselves available.
Thanks!
Tomas
Updates
Very pleased with what's coming in! Would like to see some more variety and more volume of designs.
Target Market(s)
Ages 13+ (all genders, races, creeds, income levels, etc)
Coding
Coded - Design and coding required
Number of Pages Required
5+ page
Font styles to use
Colors
Designer to choose colors to be used in the design.
Look and feel
Each slider illustrates characteristics of the customer's brand and the style your logo design should communicate.

```html
<!DOCTYPE html>
<html lang="en">
<head>
<meta charset="utf-8">
<title>JumpKOV.tv – Thank you for signing up</title>
<link rel="stylesheet" href="https://fonts.googleapis.com/css2?family=Nunito+Sans:wght@300;400;700;800&display=swap">
<style>
  :root {
    --navy: #1f2c55;
    --chrome: #2e3238;
    --chrome-text: #d9dbde;
    --bt-blue: #3d9be9;
    --page: #ffffff;
  }
  * { margin: 0; padding: 0; box-sizing: border-box; }
  html, body {
    width: 1200px; height: 2598px; overflow: hidden;
    background: var(--page);
    font-family: "Nunito Sans", "Avenir Next", sans-serif;
    color: var(--navy);
  }
  .screen { position: relative; width: 1200px; height: 2598px; }

  .status-bar {
    position: absolute; top: 0; left: 0; width: 1200px; height: 56px;
    background: var(--chrome); color: var(--chrome-text);
    font-size: 23px; font-weight: 400;
  }
  .status-bar .signal { position: absolute; left: 54px; top: 17px; }
  .status-bar .wifi { position: absolute; left: 160px; top: 13px; }
  .status-bar .clock { position: absolute; left: 0; width: 1142px; top: 12px; text-align: center; }
  .status-bar .bluetooth { position: absolute; left: 1008px; top: 13px; }
  .status-bar .battery-level { position: absolute; left: 1056px; top: 12px; }
  .status-bar .battery { position: absolute; left: 1114px; top: 15px; }

  .brand { position: absolute; left: 55px; top: 180px; }
  .brand-name {
    font-size: 62px; font-weight: 800; letter-spacing: -1px; line-height: 1;
    color: var(--navy);
  }
  .brand-tagline {
    margin-top: 14px;
    font-size: 22px; font-weight: 400; color: var(--navy); letter-spacing: 1px;
  }

  .confirmation {
    position: absolute; left: 0; top: 905px; width: 1200px; text-align: center;
  }
  .confirmation h1 {
    font-size: 78px; font-weight: 800; letter-spacing: 0.5px; line-height: 1.1;
  }
  .confirmation .message {
    margin-top: 34px;
    font-size: 51px; font-weight: 400; line-height: 68px; letter-spacing: 0.8px;
  }
  .confirmation .message span { display: block; white-space: nowrap; }
  .confirmation .closing { margin-top: 12px; font-size: 51px; font-weight: 400; line-height: 68px; letter-spacing: 0.8px; }
  .confirmation .signature { margin-top: 18px; font-size: 48px; font-weight: 800; }

  .footer-links {
    position: absolute; left: 0; top: 2300px; width: 1200px; text-align: center;
    font-size: 42px; font-weight: 400; line-height: 79px; letter-spacing: 0.8px;
  }
  .footer-links a { color: var(--navy); text-decoration: none; }
  .footer-links .sep { margin: 0 28px; }

  .menu-bar {
    position: absolute; left: 0; top: 2492px; width: 1200px; height: 106px;
    background: var(--chrome);
    display: flex; align-items: center; justify-content: center;
  }
</style>
</head>
<body>
<div class="screen">
  <header class="status-bar">
    <svg class="signal" width="84" height="16" viewBox="0 0 84 16">
      <circle cx="8" cy="8" r="6.5" fill="#d9dbde"/>
      <circle cx="25" cy="8" r="6.5" fill="#d9dbde"/>
      <circle cx="42" cy="8" r="6.5" fill="#d9dbde"/>
      <circle cx="59" cy="8" r="6" fill="none" stroke="#d9dbde" stroke-width="1.5"/>
      <circle cx="76" cy="8" r="6" fill="none" stroke="#d9dbde" stroke-width="1.5"/>
    </svg>
    <svg class="wifi" width="30" height="24" viewBox="0 0 30 24">
      <path d="M2 9a18 18 0 0 1 26 0" fill="none" stroke="#d9dbde" stroke-width="3" stroke-linecap="round"/>
      <path d="M7 14a11 11 0 0 1 16 0" fill="none" stroke="#d9dbde" stroke-width="3" stroke-linecap="round"/>
      <circle cx="15" cy="20" r="3" fill="#d9dbde"/>
    </svg>
    <div class="clock">6:13 PM</div>
    <svg class="bluetooth" width="16" height="28" viewBox="0 0 16 28">
      <path d="M2 7l12 13-6 6V2l6 6L2 21" fill="none" stroke="#3d9be9" stroke-width="2" stroke-linejoin="round"/>
    </svg>
    <div class="battery-level">62 %</div>
    <svg class="battery" width="36" height="20" viewBox="0 0 36 20">
      <rect x="1" y="1" width="30" height="18" rx="3" fill="none" stroke="#d9dbde" stroke-width="2"/>
      <rect x="4" y="4" width="17" height="12" rx="1" fill="#d9dbde"/>
      <rect x="32" y="6" width="3" height="8" rx="1" fill="#d9dbde"/>
    </svg>
  </header>

  <div class="brand">
    <div class="brand-name">JumpKOV.tv</div>
    <div class="brand-tagline">Calm Together Club</div>
  </div>

  <main class="confirmation">
    <h1>Thank you for signing up!</h1>
    <p class="message">
      <span>Please check your email for information about</span>
      <span>how our Beta program will work and what</span>
      <span>you can expect along the way. We’re so</span>
      <span>excited to have you on the KOV Team! You’re</span>
      <span>doing a wonderful thing for the world, and</span>
      <span>we are forever grateful for you!</span>
    </p>
    <p class="closing">With love,</p>
    <p class="signature">- Marisol &amp; Tomas</p>
  </main>

  <nav class="footer-links">
    <div><a href="#">Terms and Conditions</a><span class="sep">|</span><a href="#">Privacy Policy</a></div>
    <div><a href="#">About KOV</a><span class="sep">|</span><a href="#">The KOV Team</a></div>
  </nav>

  <footer class="menu-bar">
    <svg width="48" height="48" viewBox="0 0 48 48" aria-label="Menu">
      <g fill="#ffffff">
        <circle cx="7" cy="7" r="6"/><circle cx="24" cy="7" r="6"/><circle cx="41" cy="7" r="6"/>
        <circle cx="7" cy="24" r="6"/><circle cx="24" cy="24" r="6"/><circle cx="41" cy="24" r="6"/>
        <circle cx="7" cy="41" r="6"/><circle cx="24" cy="41" r="6"/><circle cx="41" cy="41" r="6"/>
      </g>
    </svg>
  </footer>
</div>
</body>
</html>
```